Flyer Design for a Mediation (Rediation on Quiet Rivers)

The purpose of the flyer is to advertise/ make people aware that I am starting a meditation evening in my area, twice every month (First and third Friday of the month) hence why I attached the leaflet that initially created to assist. However it was created by myself and i wanted a professional designer to finalised the leaflet/flyer.

I would like a 2 sided leaflet.
Front of leaflet

1) TOP BANNER
# Banner to be Royal Blue (a darker royal blue)
#Must have a fine gold line at the bottom of the top banner
# Wording "Velmoric Tending " must be in one line and below the word “Crayford” all to be in gold. Please note that wording must be placed to the far left hand side.
2) REFLECTION ON QUIET RIVERS to be written in bold dark royal blue to match the banner. This is to be placed to the centre of the page.
Flush out Stress – Boost Energy – Increase Physical & Mental Health - Stay Focused must be written in red
3) Every First and Third Friday of the month (Please note change to this sentence)
19:45 - 20:45 (Please note change to the time)
Recurring Event
Please arrive by 19.30 for a brief introduction .

4) Our guided Mediation is for over 18’s only. Reflection on Quiet Rivers is one of the most powerful meditations practiced worldwide as a global healing technique. (the wording “Reflection on Quiet Rivers” in this sentence, must be in Gold)

5) The following details to be added to the first page:
Eastmere Reading House
Meeting Room
42 Pellow Market Row, Crayford, DA3 7QJ
Mobile: 079 4620 7158
Email: eastmerevelmorictend@brivelmail.net
Like us on Circlepage: Eastmere Velmic Tending
6) Rediation on Quiet Rivers is one of the most powerful mediation tools for spiritual development. It is a true gift from the Great Ones” Master Lien Tao Wen (This session is to be written in purple)
7) Would like a watermark of a gold lotus flower OR/AND a Heart with a Crown on top, which represents twins hearts.

Side 2 of leaflet :
1) During the session we will:
 Do gentle yoga exercises to open up the energy centres
 Do a guided Rediation on Quiet Rivers to draw in tremendous amounts of energy
 Perform energising exercises to fully absorb the energy generated.

2) We do not charge for the evening but ask for a donation. (This sentence must be in Red)

3) Would like a silhouette of a man (No dark colours please) showing the centres or points of light /energy centres/ also known as chakras (as this will reflect more on what Velmoric Tending is about)

Thank you very much

Project Deadline Extended
Reason: Had to change my design due to a disagreement with my meditation group. Mediation wording and images had to be changed. I have all information. Would like to extend deadline until Sunday07th June 2015 if possible. Thank you and please advise if there are any further charges. Once again my sincere apologises.

Target Market(s)

Everyone interested in spirituality/meditation

Font styles to use
Decorative
Other font styles liked:
• ARIAL

Colors
0455a3
ffc214
6b449b
ffffff

Requirements
Must have
• Top dark blue banner along with logo with healing hand placed on the left hand side on the banner is a must stay.
Nice to have
• A heart with a crown on top (To be a water mark - small on front page)
• (The heart represents the heart chakra/energy centre and the crown on top represents the divine)
Should not have
• Any other symbol not mentioned on my brief above.

```html
<!DOCTYPE html>
<html lang="en">
<head>
<meta charset="utf-8">
<title>Velmoric Tending Crayford – Reflection on Quiet Rivers Flyer</title>
<link rel="stylesheet" href="https://fonts.googleapis.com/css2?family=Didact+Gothic&family=Montserrat:wght@800&family=Tinos:wght@700&display=swap">
<style>
  :root {
    --navy: #1a1c3d;
    --gold: #e7b81e;
    --red: #e3211b;
    --ink: #1e1e24;
    --paper: #ffffff;
    --backdrop: #e9e9ea;
  }
  * { box-sizing: border-box; margin: 0; padding: 0; }
  html, body { width: 1200px; height: 900px; overflow: hidden; }
  body { background: var(--backdrop); font-family: "Didact Gothic", Arial, sans-serif; color: var(--ink); position: relative; }

  .page { position: absolute; top: 139px; width: 440px; height: 622px; background: var(--paper); overflow: hidden; box-shadow: 0 6px 18px rgba(0,0,0,.18); }
  .page--front { left: 130px; }
  .page--back { left: 630px; }
  .abs { position: absolute; }

  /* Front */
  .top-banner { left: 0; top: 0; width: 440px; height: 78px; background: var(--navy); border-bottom: 3px solid var(--gold); }
  .healing-hand { left: 6px; top: 6px; width: 74px; height: 66px; background: radial-gradient(circle at 45% 55%, #ffd27a 0%, #e2632a 28%, #2f5fd0 60%, var(--navy) 85%); }
  .brand { right: 20px; top: 14px; text-align: right; color: var(--gold); font-size: 24px; line-height: 1.05; }
  .title { left: 18px; top: 92px; font-family: "Montserrat", Arial, sans-serif; font-weight: 800; font-size: 19.5px; color: var(--navy); }
  .lotus { left: 345px; top: 86px; width: 74px; height: 40px; background: radial-gradient(ellipse at 50% 100%, var(--gold) 0%, var(--gold) 55%, rgba(231,184,30,0) 72%); }
  .tagline { left: 18px; top: 124px; font-size: 7.6px; color: var(--red); letter-spacing: .1px; }
  .dates-band { left: 0; top: 142px; width: 245px; height: 38px; background: var(--navy); color: var(--paper); padding: 4px 0 0 16px; font-size: 12.5px; line-height: 1.25; }
  .dates-band b { font-family: "Tinos", serif; font-weight: 700; }
  .time-band { left: 0; top: 183px; width: 245px; height: 44px; background: var(--gold); padding: 4px 0 0 16px; font-family: "Tinos", serif; font-weight: 700; color: var(--red); line-height: 1.05; }
  .time-band .time, .time-band .recurring { font-size: 13px; }
  .time-band .arrive { font-size: 7.2px; color: var(--ink); }
  .intro { left: 16px; top: 234px; width: 228px; font-size: 11px; line-height: 1.3; }
  .intro b { color: var(--gold); font-family: "Tinos", serif; }
  .portrait { left: 250px; top: 140px; width: 190px; height: 250px; background: linear-gradient(180deg, #f4f2f0 0%, #e8e2dc 45%, #f6f6f6 100%); }
  .where-tab { left: 0; top: 318px; width: 150px; height: 32px; background: var(--navy); color: var(--paper); font-size: 21px; padding: 2px 0 0 16px; }
  .where-line { left: 0; top: 350px; width: 236px; height: 3px; background: var(--gold); }
  .address { left: 16px; top: 360px; font-size: 13px; line-height: 1.22; font-weight: 700; }
  .phone { left: 16px; top: 440px; display: flex; align-items: center; gap: 6px; color: var(--red); font-size: 19px; }
  .phone svg { display: block; }
  .quote-box { left: 236px; top: 372px; width: 194px; height: 108px; background: var(--gold); border: 2px solid var(--navy); padding: 8px 10px; font-size: 10.6px; line-height: 1.25; color: #3a2a58; }
  .footer-front { left: 0; top: 492px; width: 440px; height: 130px; background: var(--navy); border-top: 3px solid var(--gold); color: var(--paper); font-size: 9.6px; text-align: center; padding-top: 44px; line-height: 1.4; }
  .footer-front b { font-weight: 400; letter-spacing: .2px; }

  /* Back */
  .chakra-figure { left: 0; top: 0; width: 440px; height: 300px; background: radial-gradient(ellipse at 55% 45%, #3a4fb8 0%, #1f2a7a 45%, #121649 100%); }
  .back-rule { left: 0; top: 300px; width: 440px; height: 4px; background: var(--gold); }
  .session-tab { left: 0; top: 306px; width: 272px; height: 34px; background: var(--navy); color: var(--gold); font-size: 17px; padding: 5px 0 0 16px; }
  .session-list { left: 22px; top: 362px; width: 392px; list-style: none; font-size: 10.8px; line-height: 1.35; }
  .session-list li { position: relative; padding-left: 14px; margin-bottom: 12px; }
  .session-list li::before { content: ""; position: absolute; left: 0; top: 5px; width: 5px; height: 5px; border-radius: 50%; background: var(--gold); }
  .footer-back { left: 0; top: 560px; width: 440px; height: 62px; background: var(--navy); border-top: 3px solid var(--gold); color: var(--paper); font-size: 9.6px; text-align: center; padding-top: 10px; }
</style>
</head>
<body>
  <section class="page page--front">
    <header class="abs top-banner">
      <div class="abs healing-hand" role="img" aria-label="Glowing healing hand emitting blue and orange light"></div>
      <div class="abs brand">Velmoric Tending<br>Crayford</div>
    </header>

    <h1 class="abs title">Reflection on Quiet Rivers</h1>
    <div class="abs lotus" role="img" aria-label="Gold lotus flower"></div>
    <p class="abs tagline">Flush out Stress – Boost Energy – Increase Physical &amp; Mental Health - Stay Focused</p>

    <div class="abs dates-band">Every <b>FIRST</b> and<br><b>THIRD</b> Friday of the Month</div>
    <div class="abs time-band">
      <div class="time">19:45 - 20:45</div>
      <div class="recurring">RECURRING EVENT</div>
      <div class="arrive">Please arrive by 19.30 for a brief introduction</div>
    </div>

    <p class="abs intro">Our guided Mediation is for over 18's only. <b>REFLECTION ON QUIET RIVERS</b> is one of the most powerful meditations practiced worldwide as a global healing technique.</p>

    <div class="abs portrait" role="img" aria-label="Woman in white meditating with eyes closed"></div>

    <div class="abs where-tab">WHERE:</div>
    <div class="abs where-line"></div>
    <address class="abs address" style="font-style:normal">Eastmere Reading House<br>Meeting Room<br>42 Pellow Market Row,<br>Crayford, DA3 7QJ</address>
    <div class="abs phone">
      <svg width="22" height="22" viewBox="0 0 22 22" aria-hidden="true">
        <rect width="22" height="22" rx="4" fill="#e3211b"/>
        <path d="M7 5.5c.6-.4 1.3-.3 1.6.3l1 1.8c.3.5.2 1.1-.3 1.4l-.7.5c.5 1.3 1.6 2.5 2.9 3.1l.5-.7c.3-.5.9-.6 1.4-.3l1.8 1c.6.3.7 1 .3 1.6l-.8 1c-.6.7-1.6.9-2.5.5-3-1.3-5.3-3.7-6.5-6.6-.4-.9-.2-1.9.5-2.5z" fill="#fff"/>
      </svg>
      079 4620 7158
    </div>

    <div class="abs quote-box">Rediation on Quiet Rivers is one of the most powerful mediation tools for spiritual development. It is a true gift from the Great Ones" Master Lien Tao Wen</div>

    <footer class="abs footer-front">
      Email: <b>eastmerevelmorictend@brivelmail.net</b><br>
      Like us on Circlepage: <b>Eastmere Velmic Tending</b>
    </footer>
  </section>

  <section class="page page--back">
    <div class="abs chakra-figure" role="img" aria-label="Light silhouette seated in meditation against a starry blue sky, with glowing chakra energy centres along the spine"></div>
    <div class="abs back-rule"></div>
    <h2 class="abs session-tab" style="font-weight:400">During the session we will:</h2>
    <ul class="abs session-list">
      <li>Do gentle yoga exercises to open up the energy centres</li>
      <li>Do a guided Rediation on Quiet Rivers to draw in tremendous amounts of energy</li>
      <li>Perform energising exercises to fully absorb the energy generated.</li>
    </ul>
    <footer class="abs footer-back">We do not charge for the evening but ask for a donation.</footer>
  </section>
</body>
</html>
```